6' Banner Stands for exhibiting to Health Fairs with an audience of age 55+

We need designs for two 6' banner stands to stand on either side of our exhibition tables. We offer Hereditary Cancer Screening. I want the banners to have the same look and feel as the logo and the files color scheme logo, etc..

The Banners should have "Hereditary Cancer Screening" at the top with the Tag Line "The Test You Take For Them" underneath. A photo of grandparents with kids/grandkids and underneath the photos in large font one of the following messages:
1) "A Simple Swab Could Save A Family Members LIFE Get Tested Today!"
2) "Does Cancer Run In Your Family? Get Tested Today!"
3) "Knowledge Is Power" "Get Tested Today!"
4) "Will You Give Your Loved Ones The Information To Beat Cancer In Their Lives? Get Tested Today!
5) Knowledge Is Power Get Tested Today!"
Updates

Thank you all for your designs I now have the exact specs for the banners, so please use these as you update your designs. 31.5 inches X 83.25 inches and add a 1/2 inch bleed to all 4 sides. Thank you.

Target Market(s)

Persons 55+ who are grandparents

Industry/Entity Type

Healthcare

Font styles to use
Sans Serif
Other font styles liked:
• Comic Sans for "The Test You Take For Them"

Colors
9bcb3c
0356a4
ffffff

Requirements
Must have
• the main focus should be the hereditary cancer screening; "Hereditary Cancer Screening";
• "The test you order for them" in Comic Sans font underneath
• A photo or photos of grandparents with their grandchildren (multiple ethnicities)
• One of the slogans listed above
• GET TESTED TODAY underneath the messages at the bottom of the banner highlighted and eye catching
• www.kinwellpanel.example
Nice to have
• Logo at the top or bottom

```html
<!DOCTYPE html>
<html lang="en">
<head>
<meta charset="utf-8">
<title>Hereditary Cancer Screening – Banner Stand</title>
<link href="https://fonts.googleapis.com/css2?family=Montserrat:wght@400;600;700;800&family=Comic+Neue:wght@700&display=swap" rel="stylesheet">
<style>
  :root {
    --green: #9bcb3c;
    --blue: #0356a4;
    --white: #ffffff;
    --backdrop: #6f6f6f;
    --sans: "Montserrat", Arial, sans-serif;
    --casual: "Comic Neue", "Comic Sans MS", cursive;
  }
  * { box-sizing: border-box; margin: 0; padding: 0; }
  html, body {
    width: 1200px;
    height: 2419px;
    overflow: hidden;
    background: var(--backdrop);
  }
  .banner {
    position: absolute;
    left: 240px;
    top: 129px;
    width: 723px;
    height: 2165px;
    background: var(--white);
    overflow: hidden;
    font-family: var(--sans);
  }
  .band { position: absolute; left: 0; width: 100%; }
  .top-band { top: 0; height: 68px; background: var(--green); }
  .top-chevron { position: absolute; top: 68px; left: 0; width: 723px; height: 50px; }

  .headline {
    position: absolute;
    top: 126px;
    left: 0;
    width: 100%;
    text-align: center;
    color: var(--blue);
    font-weight: 800;
    line-height: 1;
    text-transform: uppercase;
  }
  .headline .line-small { display: block; font-size: 50px; letter-spacing: 0.5px; }
  .headline .line-large { display: block; font-size: 89px; margin-top: 2px; letter-spacing: 0.5px; }

  .tagline {
    top: 285px;
    height: 50px;
    background: var(--green);
    color: var(--white);
    font-family: var(--casual);
    font-weight: 700;
    font-size: 36px;
    letter-spacing: 2px;
    text-transform: uppercase;
    display: flex;
    align-items: center;
    justify-content: center;
  }

  .photo { position: absolute; left: 0; width: 100%; }
  .photo-embrace {
    top: 344px;
    height: 640px;
    background: linear-gradient(120deg, #f3ede6 0%, #e9c9ae 40%, #d9b095 60%, #e8e6e4 80%, #3c5f8e 100%);
  }
  .divider-green { top: 984px; height: 10px; background: var(--green); }
  .photo-garden {
    top: 1000px;
    height: 440px;
    background: linear-gradient(180deg, #5f7f3a 0%, #8aa25a 35%, #d9b8c4 60%, #c9cfe0 80%, #7aa03e 100%);
  }
  .lower-chevron { position: absolute; top: 1300px; left: 0; width: 723px; height: 260px; }

  .rule-blue { top: 1556px; height: 8px; background: var(--blue); }
  .question-top {
    top: 1581px;
    height: 72px;
    background: var(--green);
    color: var(--white);
    font-weight: 800;
    font-size: 50px;
    text-transform: uppercase;
    display: flex; align-items: center; justify-content: center;
  }
  .question-bottom {
    top: 1655px;
    height: 110px;
    color: var(--green);
    font-weight: 400;
    font-size: 74px;
    text-transform: uppercase;
    display: flex; align-items: center; justify-content: center;
  }
  .call-to-action {
    top: 1766px;
    height: 133px;
    background: var(--blue);
    color: var(--white);
    font-weight: 800;
    font-size: 54px;
    text-transform: uppercase;
    display: flex; align-items: center; justify-content: center;
  }

  .brand {
    position: absolute;
    top: 1940px;
    left: 0;
    width: 100%;
    display: flex;
    align-items: center;
    justify-content: center;
    gap: 18px;
  }
  .brand-dot { width: 100px; height: 100px; border-radius: 50%; background: var(--blue); }
  .brand-name {
    color: var(--blue);
    font-weight: 600;
    font-size: 30px;
    line-height: 1.05;
    text-transform: uppercase;
    letter-spacing: 1px;
  }

  .rule-blue-foot { top: 2073px; height: 8px; background: var(--blue); }
  .footer {
    top: 2084px;
    height: 81px;
    background: var(--green);
    color: var(--white);
    font-size: 23px;
    font-weight: 400;
    display: flex; align-items: center; justify-content: center;
  }
</style>
</head>
<body>
  <main class="banner">
    <div class="band top-band"></div>
    <svg class="top-chevron" viewBox="0 0 723 50" aria-hidden="true">
      <polygon points="0,0 723,0 723,26 410,26 361.5,48 313,26 0,26" fill="#0356a4"/>
    </svg>

    <h1 class="headline">
      <span class="line-small">Hereditary Cancer</span>
      <span class="line-large">Screening</span>
    </h1>
    <p class="band tagline">The test you take for them</p>

    <div class="photo photo-embrace" role="img" aria-label="Photo of a smiling grandmother hugging her young granddaughter"></div>
    <div class="band divider-green"></div>
    <div class="photo photo-garden" role="img" aria-label="Photo of grandparents sitting on a garden lawn with two grandchildren and a dog"></div>
    <svg class="lower-chevron" viewBox="0 0 723 260" aria-hidden="true">
      <polygon points="0,100 361.5,192 723,100 723,260 0,260" fill="#ffffff"/>
      <polygon points="0,52 361.5,152 723,52 723,100 361.5,192 0,100" fill="#0356a4"/>
      <polygon points="0,18 361.5,118 723,18 723,52 361.5,152 0,52" fill="#9bcb3c"/>
    </svg>

    <div class="band rule-blue"></div>
    <p class="band question-top">Does cancer run in</p>
    <p class="band question-bottom">Your family?</p>
    <p class="band call-to-action">Get tested today!</p>

    <div class="brand">
      <div class="brand-dot"></div>
      <div class="brand-name">Kinwell<br>Health<br>Group</div>
    </div>

    <div class="band rule-blue-foot"></div>
    <p class="band footer">www.kinwellpanel.example</p>
  </main>
</body>
</html>
```